For Sale Sign for Real Estate Agency

We need a For Sale Sign designed for our agency. I want a very simple/elegant sign that says "For Sale" towards the top of the sign (not in huge letters). Most of the sign should be a design/picture with our name and phone number somewhere at the bottom.

One significant detail, it's important that our logo not be too big or the center piece of the sign. Since our company name has the word "rent" in it, people assume the house is for rent, instead of for sale.

I attached our logo and a rough outline of the format I'm looking for.

Again, I'm looking for elegant and simple! Thanks for your time

Industry/Entity Type

Real Estate

Colors

Designer to choose colors to be used in the design.

Requirements
Must have
Nice to have
Should not have
• Nothing tacky!
• Our logo/company name should not be too big or the center piece of the sign. Since our company name has the word "rent" in it, people assume the house is for rent, instead of for sale.

```html
<!DOCTYPE html>
<html lang="en">
<head>
<meta charset="utf-8">
<title>For Sale Sign</title>
<link rel="stylesheet" href="https://fonts.googleapis.com/css2?family=Exo+2:wght@400;700&display=swap">
<style>
  :root {
    --page-bg: #e6e9ee;
    --sign-red: #e23a3f;
    --sign-red-deep: #c9262c;
    --sign-black: #121212;
    --sign-white: #ffffff;
    --brand-ink: #1c1c1c;
    --photo-sky: #9cbde0;
    --photo-house: #c9ccd0;
    --photo-lawn: #5f9a3c;
  }
  * { margin: 0; padding: 0; box-sizing: border-box; }
  html, body {
    width: 1200px;
    height: 800px;
    overflow: hidden;
    background: var(--page-bg);
  }
  .canvas {
    width: 1200px;
    height: 800px;
    display: flex;
    align-items: center;
    justify-content: center;
  }
  .sign {
    width: 400px;
    height: 700px;
    display: flex;
    flex-direction: column;
    background: var(--sign-white);
    box-shadow: 0 6px 24px rgba(0, 0, 0, 0.18);
  }
  .sign-header {
    height: 140px;
    background: linear-gradient(180deg, var(--sign-red) 0%, var(--sign-red-deep) 100%);
    display: flex;
    align-items: center;
    justify-content: center;
  }
  .sign-title {
    font-family: "Exo 2", sans-serif;
    font-weight: 700;
    font-size: 38px;
    letter-spacing: 1px;
    color: var(--sign-white);
    text-transform: uppercase;
  }
  .header-stripe {
    height: 14px;
    background: var(--sign-black);
  }
  .stripe-gap {
    height: 6px;
    background: var(--sign-white);
  }
  .property-photo {
    height: 290px;
    background: linear-gradient(180deg, var(--photo-sky) 0%, var(--photo-house) 55%, var(--photo-lawn) 88%);
  }
  .brand-area {
    height: 150px;
    display: flex;
    align-items: center;
    justify-content: center;
    background: var(--sign-white);
  }
  .brand-name {
    font-family: "Exo 2", sans-serif;
    font-weight: 400;
    font-size: 40px;
    letter-spacing: -0.5px;
    color: var(--brand-ink);
  }
  .accent-line {
    height: 6px;
    background: var(--sign-red);
  }
  .contact-band {
    height: 94px;
    background: var(--sign-black);
    display: flex;
    align-items: center;
    justify-content: center;
  }
  .contact-phone {
    font-family: "Exo 2", sans-serif;
    font-weight: 700;
    font-size: 38px;
    letter-spacing: 0.5px;
    color: var(--sign-white);
  }
</style>
</head>
<body>
  <main class="canvas">
    <section class="sign">
      <header class="sign-header">
        <h1 class="sign-title">For Sale</h1>
      </header>
      <div class="header-stripe"></div>
      <div class="stripe-gap"></div>
      <div class="property-photo" role="img" aria-label="Photo of a large shingled house with a white balcony and deck, green lawn and trees under a blue sky"></div>
      <div class="brand-area">
        <p class="brand-name">LetMark Realty</p>
      </div>
      <div class="accent-line"></div>
      <footer class="contact-band">
        <p class="contact-phone">401-555-0147</p>
      </footer>
    </section>
  </main>
</body>
</html>
```